RWM Electrical Business Card Design

Have a logo to use, just looking for design around this, would like green theme, would like symbols in place of phone, fax, email etc.

Business

RWM Electrical, Marcus Thorley, marcus@rwmelectrical.example.au, www.rwmelectrical.example.au, mobile 0491 568 342, phone (07) 3915 4280, fax (07) 3915 4280, facebook and linkedin
addresses

```html
<!DOCTYPE html>
<html lang="en">
<head>
<meta charset="utf-8">
<title>RWM Electrical Business Card</title>
<link rel="stylesheet" href="https://fonts.googleapis.com/css2?family=Questrial&display=swap">
<style>
  :root {
    --stage: #d9d9d9;
    --card-white: #ffffff;
    --card-black: #141414;
    --card-black-deep: #0a0a0a;
    --green: #45b649;
    --text-light: #f2f2f2;
    --text-dark: #2a2a2a;
  }
  * { box-sizing: border-box; margin: 0; padding: 0; }
  html, body { width: 1200px; height: 900px; overflow: hidden; }
  body {
    background: var(--stage);
    font-family: "Questrial", "Century Gothic", sans-serif;
    display: flex;
    align-items: center;
    justify-content: center;
    gap: 60px;
  }
  .card {
    width: 500px;
    height: 286px;
    border-radius: 18px;
    overflow: hidden;
    position: relative;
    box-shadow: 0 10px 24px rgba(0,0,0,0.22);
  }
  .card-front { background: var(--card-black); display: flex; flex-direction: column; }
  .front-top {
    background: var(--card-white);
    height: 112px;
    display: flex;
    align-items: center;
    padding-left: 26px;
  }
  .green-rule { height: 10px; background: var(--green); }
  .front-bottom {
    flex: 1;
    background: linear-gradient(180deg, var(--card-black), var(--card-black-deep));
    padding: 8px 26px;
  }
  .wordmark {
    display: flex;
    align-items: center;
    gap: 14px;
    font-size: 44px;
    line-height: 1;
    color: var(--green);
    white-space: nowrap;
  }
  .wordmark .mark-dot {
    width: 46px; height: 46px; border-radius: 50%;
    background: var(--green);
    flex: none;
  }
  .holder-name { color: var(--green); font-size: 15px; margin-bottom: 10px; }
  .contact-list { list-style: none; }
  .contact-list li {
    display: flex; align-items: center; gap: 5px;
    color: var(--text-light);
    font-size: 12px;
    line-height: 15px;
  }
  .contact-list svg { width: 11px; height: 11px; flex: none; fill: var(--green); }
  .card-back {
    background: radial-gradient(ellipse at 45% 40%, #262626, var(--card-black-deep) 75%);
    display: flex; align-items: center; justify-content: center;
  }
  .card-back .wordmark { font-size: 46px; }
</style>
</head>
<body>
  <section class="card card-front" aria-label="Card front">
    <div class="front-top">
      <div class="wordmark"><span class="mark-dot"></span>RWM Electrical</div>
    </div>
    <div class="green-rule"></div>
    <div class="front-bottom">
      <p class="holder-name">Marcus Thorley</p>
      <ul class="contact-list">
        <li><svg viewBox="0 0 12 12" aria-label="Mobile"><rect x="3" y="0.5" width="6" height="11" rx="1"/></svg>0491 568 342</li>
        <li><svg viewBox="0 0 12 12" aria-label="Phone"><path d="M2 1l2.5 0 1 3-1.5 1a6 6 0 0 0 3 3l1-1.5 3 1v2.5a1 1 0 0 1-1 1A10 10 0 0 1 1 2a1 1 0 0 1 1-1z"/></svg>(07) 3915 4280</li>
        <li><svg viewBox="0 0 12 12" aria-label="Fax"><rect x="3" y="0.5" width="6" height="4"/><rect x="0.5" y="4.5" width="11" height="5" rx="1"/><rect x="3" y="8" width="6" height="3.5"/></svg>(07) 3915 4280</li>
        <li><svg viewBox="0 0 12 12" aria-label="Email"><path d="M0.5 2.5h11v7h-11z M0.5 2.5l5.5 4 5.5-4" stroke="#141414" stroke-width="0.8"/></svg>marcus@rwmelectrical.example.au</li>
        <li><svg viewBox="0 0 12 12" aria-label="Web"><circle cx="6" cy="6" r="5.5"/><path d="M0.5 6h11M6 0.5v11M2 3h8M2 9h8" stroke="#141414" stroke-width="0.7" fill="none"/></svg>www.rwmelectrical.example.au</li>
        <li><svg viewBox="0 0 12 12" aria-label="Social page"><rect x="0.5" y="0.5" width="11" height="11" rx="1.5"/></svg>facepage.example\rwmelectrical</li>
        <li><svg viewBox="0 0 12 12" aria-label="Professional profile"><rect x="0.5" y="0.5" width="11" height="11" rx="1.5"/></svg>worklink.example\marcusthorley</li>
      </ul>
    </div>
  </section>
  <section class="card card-back" aria-label="Card back">
    <div class="wordmark"><span class="mark-dot"></span>RWM Electrical</div>
  </section>
</body>
</html>
```